Halvern Networks web design

Halvern is an Internet Service Provider bringing high-speed service to homes and businesses. Our principal market target is rural areas of West Michigan, but we intend to expand rapidly. We need a website to market our services, facilitate online ordering, customer support and communicate with our customers.

I will upload a draft outline of the content we hope to include in the website.

We compete directly with Brightmoor Communications, Quellix, Dunmark and Palisade communications to bring Internet service to homes and businesses in our coverage area.

Our primary values include:

1. Unlike our competitors, we do not require long term contractors or service bundles; There are no termination fees, for example. All services are sold on a recurring 1-month agreement term.
2. Unlike other wireless (mobile) providers, we do not limit downloads or uploads with bit/byte buckets
3. We provide service to areas ignored by the larger carriers - Rural areas in Michigan that lack options for broadband are prime targets for Halvern to cover.
4. Unlike other wireless ISP's, we utilize licensed FCC spectrum. We do not use unlicensed/free frequencies, providing us an advantage for reliability and stability.
Updates

So many wonderful designs, thank you very much for all your hard work. We are evaluating all our favorite designs and plan to make a selection in the next 2 days. I will be in touch with you to request revisions if necessary or further refinements.  Thank you again for your efforts on this project.

Target Market(s)

Our target market is home Internet users. however, that does not mean that our users are "high tech" oriented - they are just normal mom's and pop's who buy Internet for home use. The site should be easy to navigate and communicate our message of speed, value, reliability and facilitate simple product ordering.

Industry/Entity Type

Internet

Requirements
Must have
• Our phone number should be prominently displayed 1-844-7RU-NWAY
• Our logo is uploaded in the attachments.
• Design for desktop and mobile devices.
Nice to have
• The most modern of web design trends. Such as a design that facilitates parallax scrolling effects rather than lots of individual pages.
• Stock artwork communicating our values of speed and reliability.

```html
<!DOCTYPE html>
<html lang="en">
<head>
<meta charset="utf-8">
<title>Halvern Networks — West Michigan's Best Internet Service</title>
<link rel="stylesheet" href="https://fonts.googleapis.com/css2?family=Roboto:wght@300;400;500;700&family=Open+Sans:ital,wght@0,400;0,600;1,400&display=swap">
<style>
:root{
  --orange:#f7861e;
  --orange-deep:#f2711c;
  --ink:#333;
  --muted:#777;
  --line:#e3e3e3;
  --band:#f6f6f6;
  --dark:#4a4a4a;
  --white:#fff;
}
*{box-sizing:border-box;margin:0;padding:0}
html,body{width:1200px;height:2663px;overflow:hidden}
body{font-family:"Open Sans",Arial,sans-serif;color:var(--ink);background:var(--white);position:relative}
.abs{position:absolute}
.brand{font-family:"Roboto",Arial,sans-serif;font-weight:700;color:var(--orange);letter-spacing:1px;text-transform:uppercase;line-height:1}

/* header */
.site-header{position:absolute;left:0;top:0;width:1200px;height:80px;background:var(--white);border-bottom:1px solid var(--line)}
.site-header .brand{left:135px;top:22px;font-size:30px}
.lang-pill{left:493px;top:26px;width:57px;height:26px;border:1px solid #ccc;border-radius:13px;display:flex;align-items:center;justify-content:center;gap:4px}
.top-phone{left:577px;top:31px;font-size:13px;color:#999;font-family:"Roboto",sans-serif}
.main-nav{left:715px;top:20px;height:40px;display:flex;font-family:"Roboto",sans-serif;font-size:12.5px}
.main-nav a{display:block;padding:0 22px;line-height:40px;color:var(--ink);text-decoration:none;border-left:1px solid var(--line)}
.main-nav a.active{color:var(--orange)}

/* hero */
.hero{position:absolute;left:0;top:80px;width:1200px;height:580px;background:linear-gradient(100deg,#cfc8bc 0%,#ece8e2 35%,#c7c9c6 60%,#9e9a90 100%)}
.hero-title{position:absolute;left:135px;background:var(--orange);color:var(--white);font-family:"Roboto",sans-serif;font-weight:500;font-size:31px;padding:5px 10px;line-height:46px}
.hero-lede{position:absolute;left:135px;top:234px;width:518px;background:rgba(60,60,60,.75);color:#f2f2f2;font-size:15.5px;line-height:25px;padding:3px 8px}
.benefits{position:absolute;left:135px;top:310px;list-style:none;font-family:"Roboto",sans-serif;font-size:18px;color:#111}
.benefits li{height:31.5px;display:flex;align-items:center;gap:12px}

/* bands */
.band{position:absolute;left:0;width:1200px;background:var(--band);border-top:1px solid var(--line);border-bottom:1px solid var(--line);display:flex;align-items:center;justify-content:center;font-family:"Roboto",sans-serif;color:#333}

/* pricing */
.pricing{position:absolute;left:0;top:755px;width:1200px;height:438px;background:#fafafa}
.section-title{position:absolute;width:100%;text-align:center;font-family:"Roboto",sans-serif;font-size:26px;color:#444}
.carousel-arrows{position:absolute;left:1015px;top:40px;display:flex;gap:14px}
.plan-card{position:absolute;left:245px;top:90px;width:653px;height:360px;background:var(--white);border:1px solid #e5e5e5;border-radius:24px 24px 0 0}
.plan-table{position:absolute;left:98px;top:0;width:461px;border-collapse:collapse;font-family:"Roboto",sans-serif;text-align:center}
.plan-table th{font-size:13px;font-weight:700;height:45px;padding-top:22px;color:#333}
.plan-table td{border:1px solid #ddd;font-size:11px;color:#777;height:45px;width:153px}
.plan-table .price{height:72px;color:var(--orange);font-size:32px;font-weight:700;line-height:1}
.plan-table .price small{display:block;color:#333;font-size:10px;font-weight:400;margin-top:4px}
.plan-table .price sup{font-size:22px;vertical-align:0}
.plan-table .lbl{display:block;color:var(--orange);margin-bottom:4px}

/* inside */
.inside{position:absolute;left:0;top:1282px;width:1200px;height:440px;background:linear-gradient(#fff,#f3f3f3)}
.col{position:absolute;top:100px;width:280px}
.col h3{font-family:"Roboto",sans-serif;font-weight:400;font-size:24px;color:#333;height:40px;border-bottom:1px solid var(--line);display:flex;justify-content:space-between;align-items:center}
.mini-arrows{display:flex;gap:3px}
.mini-arrows span{width:16px;height:16px;background:#e3e3e3;display:block}
.mini-arrows span+span{background:#bbb}
.news-item{display:flex;gap:10px;padding:14px 0;border-bottom:1px solid var(--line);font-size:10px;line-height:15px}
.news-thumb{width:82px;height:46px;flex:none;background:linear-gradient(135deg,#ddd,#8a6a50)}
.news-item b{color:var(--orange);font-weight:400;text-transform:uppercase;display:block}
.news-item i{color:#aaa;display:block}
.news-item p{color:#888}
.blog-item{display:flex;gap:14px;padding:16px 0;border-bottom:1px solid var(--line);font-size:10px;line-height:14px}
.date-tag{width:54px;height:54px;flex:none;background:var(--orange-deep);color:#fff;font-weight:600;font-size:12px;text-align:center;padding-top:12px;line-height:14px}
.blog-item strong{font-weight:400;font-size:12px;display:block;margin-bottom:6px}
.staff{display:flex;align-items:center;gap:12px;height:58px;border-bottom:1px solid var(--line)}
.avatar{width:44px;height:44px;border-radius:50%;background:linear-gradient(135deg,#7b5a48,#3c2a22);flex:none}
.staff div{flex:1;font-size:14px;font-weight:600}
.staff em{display:block;font-size:8.5px;font-weight:400;color:#999}

/* account */
.account{position:absolute;left:0;top:1722px;width:1200px;height:240px;background:var(--dark);display:flex}
.account section{flex:1;text-align:center;color:#fff;padding-top:54px;font-family:"Roboto",sans-serif}
.account section+section{border-left:1px solid #666}
.account h2{font-weight:400;font-size:19px}
.account p{font-size:12.5px;margin-top:6px}
.btn-light{display:inline-block;margin-top:24px;width:218px;height:44px;line-height:42px;background:#fff;border:1px solid #ccc;border-radius:3px;color:#333;font-size:14.5px}

/* coverage */
.coverage{position:absolute;left:0;top:1962px;width:1200px;height:390px;background:var(--orange);color:#fff;text-align:center;font-family:"Roboto",sans-serif}
.coverage .map{position:absolute;left:150px;top:30px;width:900px;height:340px;background:radial-gradient(ellipse at center,rgba(0,0,0,.06),rgba(0,0,0,0) 70%)}
.coverage h2{position:absolute;width:100%;top:46px;font-weight:400;font-size:27px}
.coverage .sub{position:absolute;width:100%;top:90px;font-size:13.5px}
.coverage .ask{position:absolute;width:100%;top:122px;font-size:20px}
.address-field{position:absolute;left:248px;top:179px;width:723px;height:40px;background:#fff;border:none}
.order-btn{position:absolute;left:486px;top:257px;width:259px;height:57px;border-radius:29px;background:#fff;color:var(--orange);font-size:20px;line-height:57px;box-shadow:0 0 0 5px rgba(255,255,255,.25)}

/* footer */
.site-footer{position:absolute;left:0;top:2352px;width:1200px;height:248px;background:#fff;font-family:"Roboto",sans-serif}
.f-col{position:absolute;top:40px;font-size:14px;color:#666;line-height:23.5px}
.f-col h4{color:var(--orange);font-weight:500;font-size:15.5px;border-left:3px solid var(--orange);padding-left:6px;margin-bottom:10px;line-height:18px}
.f-col ul{list-style:none;padding-left:10px}
.f-col a{color:var(--orange);text-decoration:none}
.bottom-bar{position:absolute;left:0;top:2600px;width:1200px;height:63px;border-top:1px solid var(--line);font-family:"Roboto",sans-serif}
.bottom-bar .brand{position:absolute;left:135px;top:22px;font-size:22px}
.legal{position:absolute;right:132px;top:14px;text-align:right;font-size:10.5px;color:#555;line-height:19px}
</style>
</head>
<body>

<header class="site-header">
  <div class="brand abs">Halvern Networks</div>
  <div class="lang-pill abs">
    <svg width="14" height="14" viewBox="0 0 14 14"><circle cx="7" cy="7" r="6" fill="#888"/><path d="M1 7h12M7 1c-3 3-3 9 0 12M7 1c3 3 3 9 0 12" stroke="#fff" fill="none" stroke-width="1"/></svg>
    <svg width="8" height="6" viewBox="0 0 8 6"><path d="M0 0h8L4 5z" fill="#888"/></svg>
  </div>
  <div class="top-phone abs">+1 (888) 555-0184</div>
  <nav class="main-nav abs">
    <a class="active" href="#">Home</a><a href="#">Service Plans</a><a href="#">Coverage Map</a><a href="#">About Us</a>
  </nav>
</header>

<section class="hero" role="img" aria-label="Photo of a smiling man working on a laptop at a café table with a coffee cup">
  <div class="hero-title" style="top:110px">West Michigan's</div>
  <div class="hero-title" style="top:170px">Best Internet Service</div>
  <p class="hero-lede">Halvern Networks is a Michigan-based company providing high-speed Internet services to West Michigan homes and businesses.</p>
  <ul class="benefits">
    <li><svg width="18" height="16" viewBox="0 0 18 16"><path d="M1 8l6 6L17 1" stroke="#f7861e" stroke-width="3" fill="none"/></svg>100% Satisfaction Guaranteed</li>
    <li><svg width="18" height="16" viewBox="0 0 18 16"><path d="M1 8l6 6L17 1" stroke="#f7861e" stroke-width="3" fill="none"/></svg>Honest Pricing, No Hidden Fees</li>
    <li><svg width="18" height="16" viewBox="0 0 18 16"><path d="M1 8l6 6L17 1" stroke="#f7861e" stroke-width="3" fill="none"/></svg>No Long Term Contracts</li>
    <li><svg width="18" height="16" viewBox="0 0 18 16"><path d="M1 8l6 6L17 1" stroke="#f7861e" stroke-width="3" fill="none"/></svg>No Phone Line or Cable TV required</li>
    <li><svg width="18" height="16" viewBox="0 0 18 16"><path d="M1 8l6 6L17 1" stroke="#f7861e" stroke-width="3" fill="none"/></svg>Fast, Superior Performance for your home</li>
    <li><svg width="18" height="16" viewBox="0 0 18 16"><path d="M1 8l6 6L17 1" stroke="#f7861e" stroke-width="3" fill="none"/></svg>Interference-Free FCC Licensed 4G Coverage</li>
  </ul>
</section>

<div class="band" style="top:660px;height:95px;font-size:26px">Pick the Price Plan And Choose the Best Solution For You</div>

<section class="pricing">
  <h2 class="section-title" style="top:34px">Residential Plan</h2>
  <div class="carousel-arrows">
    <svg width="16" height="22" viewBox="0 0 16 22"><path d="M13 2L4 11l9 9" stroke="#bbb" stroke-width="4" fill="none"/></svg>
    <svg width="16" height="22" viewBox="0 0 16 22"><path d="M3 2l9 9-9 9" stroke="#bbb" stroke-width="4" fill="none"/></svg>
  </div>
  <div class="plan-card">
    <table class="plan-table">
      <tr><th>Best Value</th><th>Premium Value</th><th>Unlimited Value</th></tr>
      <tr><td class="price">24.99 <sup>$</sup><small>per month</small></td><td class="price">44.99 <sup>$</sup><small>per month</small></td><td class="price">74.99 <sup>$</sup><small>per month</small></td></tr>
      <tr><td><span class="lbl">Download</span>1 MB</td><td><span class="lbl">Download</span>3MB</td><td><span class="lbl">Download</span>10MB</td></tr>
      <tr><td><span class="lbl">Bandwidth</span>1MB</td><td><span class="lbl">Bandwidth</span>3MB</td><td><span class="lbl">Bandwidth</span>10MB</td></tr>
      <tr><td><span class="lbl">Usage</span>512Kbps</td><td><span class="lbl">Usage</span>1.0Mbps</td><td><span class="lbl">Usage</span>2.0 Mbps</td></tr>
      <tr><td><span class="lbl">Installations</span>$100.00 install</td><td><span class="lbl">Installations</span>$100.00 install</td><td><span class="lbl">Installations</span>$100.00 install</td></tr>
      <tr><td style="height:50px"></td><td></td><td></td></tr>
    </table>
  </div>
</section>

<div class="band" style="top:1193px;height:89px;font-size:28px;background:#f4f4f4">Inside Halvern</div>

<section class="inside">
  <div class="col" style="left:147px">
    <h3>Latest News <span class="mini-arrows"><span></span><span></span></span></h3>
    <div class="news-item"><div class="news-thumb" role="img" aria-label="Group of business people"></div><div><b>Passage of lorem ipsum.</b><i>Posted on May 20, 2013</i><p>Lorem ipsum dolor sit amet, consectetur adipiscing...</p></div></div>
    <div class="news-item" style="border:none"><div class="news-thumb" role="img" aria-label="Hands holding small figures"></div><div><b>Passage of lorem ipsum.</b><i>Posted on April 20, 2013</i><p>Sed leo enim, pellentesque nec pretium a, lobortis...</p></div></div>
  </div>
  <div class="col" style="left:456px">
    <h3>Company Blog <span class="mini-arrows"><span></span><span></span></span></h3>
    <div class="blog-item"><div class="date-tag">OCT<br>02</div><div><strong>Regular post with thumnail</strong>It is a long established fact that a reader will be distracted by the readables on purpose</div></div>
    <div class="blog-item" style="border:none"><div class="date-tag">OCT<br>02</div><div><strong>Blog post with thumnail</strong>It is a long established fact that a reader will be distracted by the readables on purpose</div></div>
  </div>
  <div class="col" style="left:772px">
    <h3><span style="margin-left:54px">Staff profiles</span> <span class="mini-arrows"><span></span><span></span></span></h3>
    <div class="staff"><span class="avatar" role="img" aria-label="Portrait of staff member"></span><div>Alina Roverton<em>Product Designer at Plinkly</em></div><svg width="14" height="12" viewBox="0 0 14 12"><path d="M1 1h12v8H5l-3 2V9H1z" stroke="#888" fill="none"/></svg></div>
    <div class="staff"><span class="avatar" role="img" aria-label="Portrait of staff member"></span><div>Marcus Jorden<em>Creative Manager at Corvex Media</em></div><svg width="14" height="12" viewBox="0 0 14 12"><path d="M1 1h12v8H5l-3 2V9H1z" stroke="#888" fill="none"/></svg></div>
    <div class="staff" style="border:none"><span class="avatar" role="img" aria-label="Portrait of staff member"></span><div>Mira Belton<em>Marketing Manager at Tessaro Systems</em></div><svg width="14" height="12" viewBox="0 0 14 12"><path d="M1 1h12v8H5l-3 2V9H1z" stroke="#888" fill="none"/></svg></div>
  </div>
</section>

<section class="account">
  <section><h2>Manage&nbsp; Your Account</h2><p>This will be a link to account management.</p><span class="btn-light">Billvane Login Page</span></section>
  <section><h2>Request Customer Support</h2><p>We use Helpmoor for customer service.</p><span class="btn-light">Request Customer Support</span></section>
</section>

<section class="coverage">
  <div class="map" role="img" aria-label="Faint world map in the background"></div>
  <h2>Coverage Map</h2>
  <p class="sub">A form to enter address to check for service availability</p>
  <p class="ask">Am I Covered?</p>
  <div class="address-field"></div>
  <div class="order-btn">ORDER NOW</div>
</section>

<footer class="site-footer">
  <div class="f-col" style="left:135px"><h4>Quick Links</h4><ul><li>Service Plans</li><li>Coverage Map</li><li>WhoisHalvern</li><li>Company Blog</li><li>Customer Support</li><li>Account Management</li></ul></div>
  <div class="f-col" style="left:486px"><h4>Get me in touch</h4><ul><li>Call today to place an</li><li>order or reach customer</li><li>support 844-7RU-NWAY</li><li>Local number 517-555-0137</li></ul><h4 style="margin-top:2px">Subscribe</h4><ul><li>Email support: <a href="#">support@halvernspeed.com</a></li></ul></div>
  <div class="f-col" style="left:895px"><h4>Support Staff Hours</h4><ul><li>Weekdays 7am to 10pm</li><li>Weekends 8am to 5pm</li><li>Holiday scheduling varies</li></ul></div>
</footer>

<div class="bottom-bar">
  <div class="brand">Halvern Networks</div>
  <div class="legal">Term of Use |&nbsp; Privacy Policy<br>2014 Halvern Network.com All Right Reserved</div>
</div>

</body>
</html>
```